Business Card Design for the Larkmoor Venous and Larkmoor Aesthetic Institute Clinics

We need one business card design for an existing company based in Chicago called Larkmoor Venous Institute and Larkmoor Aesthetic Institute. We are vein and plastic surgery clinics. There are two speared logos for each company Larkmoor Venous and Larkmoor Aesthetic Institute.Before we had two separate busniess cards for each company, but now we want to combained them into one, and thus the both logos need to be on the the card. I would like to see the design that follow the design of our brochure and folders. The colors included need to be the ones of our two logos(orange, gray and teal--> see the attachment). The design needs to represent two companies under one roof. The final design should communicate trust and loyalty

Target Market(s)

Medical

Industry/Entity Type

Medical

Contact Information for Business Card

Larkmoor Venous InstituteLarkmoor Aesthetic Institute4817 W. Dunmore Ridge Rd. Chicago, IL 60618www.larkmoorvenous-example.comwww.larkmooraesthetic-example.comTelephone (773) 555-0182Fax (773) 555-0183

Requirements
Must have
• Both logos, ultimately representing both companies at one card

```html
<!DOCTYPE html>
<html lang="en">
<head>
<meta charset="utf-8">
<title>Business Card – Larkmoor Venous & Larkmoor Aesthetic Institute</title>
<link href="https://fonts.googleapis.com/css2?family=Roboto+Condensed:wght@300;400&display=swap" rel="stylesheet">
<style>
  :root {
    --coral: #f65d50;
    --teal: #28b5a0;
    --text-gray: #555759;
    --name-gray: #8f9194;
    --paper: #ffffff;
    --canvas: #ffffff;
  }
  * { margin: 0; padding: 0; box-sizing: border-box; }
  html, body {
    width: 960px; height: 1200px; overflow: hidden;
    background: var(--canvas);
    font-family: "Roboto Condensed", "Arial Narrow", sans-serif;
  }
  .card {
    position: absolute;
    left: 61px;
    width: 838px;
    height: 478px;
    background: var(--paper);
    box-shadow: 8px 10px 14px rgba(0,0,0,0.35);
    overflow: hidden;
  }
  /* Front */
  .card--front { top: 32px; }
  .doctor {
    position: absolute; left: 39px; top: 38px;
    font-size: 50px; font-weight: 400; line-height: 1; color: var(--coral);
    letter-spacing: -0.5px; white-space: nowrap;
  }
  .doctor .credentials { color: var(--teal); font-weight: 300; }
  .doctor-title {
    position: absolute; left: 39px; top: 94px;
    font-size: 37px; font-weight: 400; line-height: 1; color: var(--text-gray);
  }
  .contact {
    position: absolute; left: 114px; top: 218px;
    font-size: 28px; font-weight: 300; line-height: 40px; color: var(--text-gray);
    list-style: none; white-space: nowrap;
  }
  .contact .accent { color: var(--coral); }
  .web-band {
    position: absolute; left: 0; bottom: 0;
    width: 100%; height: 96px;
    background: var(--teal);
  }
  .web-band__block {
    position: absolute; left: 0; top: 0;
    width: 114px; height: 100%;
    background: var(--coral);
  }
  .web-band__links {
    position: absolute; right: 24px; top: 14px;
    text-align: right; color: #fff;
    font-size: 27px; font-weight: 300; line-height: 34px;
  }
  /* Back */
  .card--back { top: 546px; }
  .back-half {
    position: absolute; left: 0; width: 100%; height: 239px;
  }
  .back-half--venous {
    top: 0;
    background: linear-gradient(to right, #3dbaa5 0px, rgba(61,186,165,0.35) 220px, rgba(255,255,255,0) 312px);
    border-bottom: 1px solid #d8d8d8;
  }
  .back-half--aesthetic {
    top: 239px;
    background: linear-gradient(to right, rgba(255,255,255,0) 524px, rgba(246,93,80,0.45) 700px, var(--coral) 838px);
  }
  .clinic-name {
    position: absolute;
    font-size: 34px; font-weight: 400; line-height: 1;
    white-space: nowrap;
  }
  .clinic-name--venous {
    right: 24px; top: 150px; color: var(--name-gray);
  }
  .clinic-name--aesthetic {
    left: 40px; top: 70px; color: var(--coral);
  }
</style>
</head>
<body>

<section class="card card--front" aria-label="Business card front">
  <h1 class="doctor">Dr. Nathaniel Corwell, <span class="credentials">MD FACS</span></h1>
  <p class="doctor-title">title goes here</p>

  <ul class="contact">
    <li>Larkmoor Venous Institute • Larkmoor Aesthetic Institute</li>
    <li>4817 W. Dunmore Ridge Rd. Chicago, IL 60618</li>
    <li>Telephone <span class="accent">(773) 555-0182</span> • Fax (773) 555-0183</li>
    <li>Email: <span class="accent">dr.nathanielcorwell@lmi-example.com</span></li>
  </ul>

  <div class="web-band">
    <div class="web-band__block"></div>
    <div class="web-band__links">
      <div>www.larkmoorvenous-example.com</div>
      <div>www.larkmooraesthetic-example.com</div>
    </div>
  </div>
</section>

<section class="card card--back" aria-label="Business card back">
  <div class="back-half back-half--venous">
    <p class="clinic-name clinic-name--venous">Larkmoor Venous Institute</p>
  </div>
  <div class="back-half back-half--aesthetic">
    <p class="clinic-name clinic-name--aesthetic">Larkmoor Aesthetic Institute</p>
  </div>
</section>

</body>
</html>
```